Business card for Financial Technology company

Hello! We'd like to create business cards for 4 members of our company. Our company is a financial technology business that provides funding for businesses. We want to give it a VC (venture captal) look and feel. Clean, fresh and minimal but with a flair of artistry. I'll include some samples of cards we like. It would be great if the back of the card was artistic (see sample files 1 and 2) and the front of the card was the business info. The name of the company is Q7 Funding.

```html
<!DOCTYPE html>
<html lang="en">
<head>
<meta charset="utf-8">
<title>Q7 Funding — Business Card</title>
<link href="https://fonts.googleapis.com/css2?family=Jost:wght@400;500;600&display=swap" rel="stylesheet">
<style>
  :root {
    --bg: #2b2b2d;
    --ink: #1c1a22;
    --magenta: #e2298a;
    --purple: #7b2f8e;
    --violet: #5a3a9a;
    --orange: #f08a2a;
    --yellow: #f6cf1c;
    --green: #3fae4a;
    --teal: #1f7a78;
    --circle: #f1f1f1;
  }
  * { box-sizing: border-box; margin: 0; padding: 0; }
  html, body { width: 1200px; height: 900px; overflow: hidden; }
  body {
    background: var(--bg);
    font-family: 'Jost', sans-serif;
    color: var(--ink);
    position: relative;
  }
  .card {
    position: absolute;
    width: 640px;
    height: 366px;
    overflow: hidden;
    box-shadow: 0 18px 40px rgba(0,0,0,.45);
  }
  .card--back  { left: 170px; top: 60px; }
  .card--front { left: 390px; top: 474px; }

  .card__art {
    position: absolute; inset: 0;
  }
  .card--back .card__art {
    background:
      radial-gradient(ellipse 30% 45% at 100% 8%, var(--green) 0%, var(--teal) 55%, transparent 100%),
      radial-gradient(ellipse 55% 40% at 45% 55%, var(--yellow) 0%, var(--orange) 45%, transparent 80%),
      linear-gradient(160deg, var(--purple) 0%, var(--magenta) 35%, var(--orange) 55%, var(--magenta) 75%, var(--violet) 100%);
  }
  .card--front .card__art {
    background:
      radial-gradient(ellipse 35% 45% at 85% 10%, #ffffff 0%, #e6f2ea 45%, transparent 100%),
      radial-gradient(ellipse 55% 40% at 45% 55%, #f7e678 0%, #f4c266 45%, transparent 80%),
      linear-gradient(165deg, #c9a4d8 0%, #eb86c3 35%, #f2b06a 55%, #ec8fc8 78%, #b88ad4 100%);
  }

  .brand-badge {
    position: absolute;
    left: 50%; top: 44%;
    transform: translate(-50%, -50%);
    width: 170px; height: 170px;
    border-radius: 50%;
    background: var(--circle);
    display: flex; align-items: center; justify-content: center;
    box-shadow: 0 2px 6px rgba(0,0,0,.15);
  }
  .brand-name {
    font-weight: 600;
    font-size: 26px;
    color: var(--ink);
    letter-spacing: .5px;
  }
  .card--front .brand-name {
    position: absolute;
    right: 40px; top: 40px;
    font-size: 24px;
  }

  .contact {
    position: absolute;
    left: 38px; bottom: 26px;
    right: 38px;
  }
  .person__name {
    font-weight: 600;
    font-size: 20px;
    letter-spacing: .5px;
    text-transform: uppercase;
  }
  .person__role {
    font-weight: 500;
    font-size: 16px;
    margin-bottom: 14px;
  }
  .contact__list { list-style: none; }
  .contact__item {
    display: flex; align-items: center; gap: 10px;
    font-weight: 500;
    font-size: 16px;
    line-height: 24px;
  }
  .contact__icon { width: 14px; height: 14px; flex: none; }
  .contact__rule {
    border: 0;
    border-top: 1.5px solid var(--ink);
    margin: 8px 0 6px;
  }
  .contact__address {
    font-weight: 500;
    font-size: 17px;
    letter-spacing: .3px;
  }
</style>
</head>
<body>

  <section class="card card--back">
    <div class="card__art" role="img" aria-label="Colourful low-poly triangle pattern in magenta, purple, orange, yellow and green"></div>
    <div class="brand-badge">
      <span class="brand-name">Q7 Funding</span>
    </div>
  </section>

  <section class="card card--front">
    <div class="card__art" role="img" aria-label="Soft pastel low-poly triangle pattern in pink, lilac and yellow"></div>
    <span class="brand-name">Q7 Funding</span>

    <div class="contact">
      <p class="person__name">Daniel Averon</p>
      <p class="person__role">Founder</p>
      <ul class="contact__list">
        <li class="contact__item">
          <svg class="contact__icon" viewBox="0 0 24 24" aria-hidden="true"><path fill="currentColor" d="M6.6 10.8a15.1 15.1 0 0 0 6.6 6.6l2.2-2.2c.3-.3.7-.4 1-.2 1.1.4 2.3.6 3.6.6.6 0 1 .4 1 1V20c0 .6-.4 1-1 1A17 17 0 0 1 3 4c0-.6.4-1 1-1h3.5c.6 0 1 .4 1 1 0 1.3.2 2.5.6 3.6.1.3 0 .7-.2 1z"/></svg>
          (888) 555-0142
        </li>
        <li class="contact__item">
          <svg class="contact__icon" viewBox="0 0 24 24" aria-hidden="true"><path fill="currentColor" d="M2 5h20v14H2zm2 2v.5l8 5 8-5V7l-8 5z"/></svg>
          info@q7funding.com
        </li>
        <li class="contact__item">
          <svg class="contact__icon" viewBox="0 0 24 24" aria-hidden="true"><g fill="none" stroke="currentColor" stroke-width="1.8"><circle cx="12" cy="12" r="9.5"/><ellipse cx="12" cy="12" rx="4" ry="9.5"/><path d="M2.5 12h19M4 7h16M4 17h16"/></g></svg>
          www.q7funding.com
        </li>
      </ul>
      <hr class="contact__rule">
      <p class="contact__address">42 Harbor Point Road, Suite 210, Fairview Heights, NJ 07010</p>
    </div>
  </section>

</body>
</html>
```